Professional Services - letterhead / business cards

The company (veltaro holdings) will provide services to Investment Funds and large investors in Spain. I have recently chosen a logo that I am attaching.

I would like a simple stationary design that i could use as letter head, business cards and "with compliments" cards.

I am not quite sure which color I will mostly use for the logo, in the email signature I will probably lean towards the white background and grey letters. I am attaching my favourite options.

Target Market(s)

Large Multinationals, Investment funds and Law firms

Industry/Entity Type

Business

Requirements
Must have
• my details are:
Luis R. Andrade
Veltaro Holdings S.L.
Casa de Valdehondo
Calle del Olmo Tardío 42
28017 Madrid
T: +34 (91) 807-3356
M: +34 (655) 718-904
e-mail: landrade@veltaroholdings.example

```html
<!DOCTYPE html>
<html lang="en">
<head>
<meta charset="utf-8">
<title>Veltaro Holdings – Stationery</title>
<link rel="stylesheet" href="https://fonts.googleapis.com/css2?family=Questrial&family=PT+Sans:ital@0;1&family=PT+Sans+Narrow&display=swap">
<style>
  :root {
    --navy: #24276a;
    --navy-deep: #1e2160;
    --royal: #2c3b98;
    --royal-band: #262f82;
    --paper: #ffffff;
    --ink: #1f2262;
    --shadow: rgba(0, 0, 0, 0.22);
  }
  * { box-sizing: border-box; margin: 0; padding: 0; }
  html, body { width: 1200px; height: 740px; overflow: hidden; background: var(--paper); }
  .canvas { position: relative; width: 1200px; height: 740px; font-family: "PT Sans", sans-serif; color: var(--ink); }
  .abs { position: absolute; }

  .wordmark { font-family: "Questrial", sans-serif; white-space: nowrap; line-height: 1; letter-spacing: 0.01em; }

  /* Card back */
  .card-back { left: 4px; top: 117px; width: 284px; height: 184px; border-radius: 10px; background: var(--royal); overflow: hidden; }
  .card-back .band { top: 83px; width: 48px; height: 27px; background: var(--royal-band); }
  .card-back .wordmark { left: 0; right: 0; top: 88px; text-align: center; color: #fff; font-size: 17px; }

  /* Business card front */
  .card-front { left: 172px; top: 307px; width: 286px; height: 185px; border-radius: 10px; background: var(--paper); box-shadow: 0 1px 6px var(--shadow); overflow: hidden; }
  .card-front .band { top: 18px; width: 48px; height: 27px; background: var(--navy); }
  .card-front .wordmark { left: 0; right: 0; top: 25px; text-align: center; font-size: 16px; color: var(--ink); }
  .card-front .holder { left: 0; right: 0; top: 73px; text-align: center; font-family: "PT Sans Narrow", sans-serif; font-size: 16px; }
  .contact-bar { background: var(--navy); color: #fff; font-size: 5.4px; line-height: 1.35; }
  .card-front .contact-bar { left: 5px; top: 123px; width: 278px; height: 45px; padding: 8px 0 0 6px; }
  .contact-bar .col { position: absolute; top: 8px; }
  .contact-bar .indent { padding-left: 1.2em; }

  /* Compliments slip */
  .slip { left: 160px; top: 490px; width: 460px; height: 245px; }
  .slip svg { position: absolute; inset: 0; }
  .slip .wordmark { left: 125px; width: 360px; text-align: center; top: 44px; font-size: 24px; color: var(--ink); }
  .slip .holder { left: 25px; top: 120px; font-family: "PT Sans Narrow", sans-serif; font-size: 22px; }
  .slip .address { left: 25px; top: 171px; font-size: 7.6px; line-height: 1.38; }
  .slip .greeting { left: 303px; top: 168px; font-style: italic; font-size: 11px; }

  /* Folder */
  .folder { left: 466px; top: 7px; width: 397px; height: 469px; background: var(--navy); box-shadow: 2px 2px 6px var(--shadow); }
  .folder .wordmark { left: 26px; top: 391px; color: #fff; font-size: 22px; }

  /* Letterhead */
  .letter { left: 772px; top: 28px; width: 418px; height: 500px; background: var(--paper); box-shadow: 0 1px 6px var(--shadow); }
  .letter .band { top: 33px; height: 11px; background: var(--navy); }
  .letter .wordmark { left: 86px; width: 249px; text-align: center; top: 29px; font-size: 21px; color: var(--ink); }
  .letter .body { left: 43px; top: 133px; width: 340px; font-size: 11px; line-height: 13px; color: #111; }
  .letter .body p + p { margin-top: 13px; }
  .letter .sign-name { right: 50px; top: 389px; font-size: 11px; color: #111; }
  .letter .signature { left: 280px; top: 406px; width: 92px; height: 22px; background: #eeeef4; }
  .letter .contact-bar { left: 0; top: 443px; width: 418px; height: 57px; font-size: 7px; }
  .letter .contact-bar .col { top: 17px; }
</style>
</head>
<body>
<main class="canvas">

  <section class="card-back abs" aria-label="Business card, back">
    <div class="band abs" style="left:0"></div>
    <div class="band abs" style="right:0"></div>
    <div class="wordmark abs">veltaro holdings</div>
  </section>

  <section class="card-front abs" aria-label="Business card, front">
    <div class="band abs" style="left:1px"></div>
    <div class="band abs" style="right:2px"></div>
    <div class="wordmark abs">veltaro holdings</div>
    <div class="holder abs">Luis R. Andrade</div>
    <div class="contact-bar abs">
      <div class="col" style="left:6px">A: Casa de Valdehondo<div class="indent">Calle del Olmo Tardío 42</div><div class="indent">28017 Madrid</div></div>
      <div class="col" style="left:110px">T: +34 (91) 807-3356<br>M: +34 (655) 718-904</div>
      <div class="col" style="left:180px">E: landrade@veltaroholdings.example</div>
    </div>
  </section>

  <section class="slip abs" aria-label="With compliments card">
    <svg width="460" height="245" viewBox="160 490 460 245" aria-hidden="true">
      <defs>
        <filter id="slip-shadow" x="-5%" y="-5%" width="110%" height="115%">
          <feDropShadow dx="1" dy="3" stdDeviation="3" flood-color="#000" flood-opacity="0.22"/>
        </filter>
      </defs>
      <path d="M169 722 V565 C169 522 200 499 250 499 H607 V640 C607 695 585 722 540 722 Z" fill="#fff" filter="url(#slip-shadow)"/>
      <path d="M170 572 V552 C170 530 186 517 214 517 H280 V572 Z" fill="#24276a"/>
      <rect x="557" y="517" width="45" height="55" fill="#24276a"/>
    </svg>
    <div class="wordmark abs">veltaro holdings</div>
    <div class="holder abs">Luis R. Andrade</div>
    <div class="address abs">Casa de Valdehondo<br>Calle del Olmo Tardío 42<br>28017 Madrid</div>
    <div class="greeting abs">With Compliments</div>
  </section>

  <section class="folder abs" aria-label="Presentation folder">
    <div class="wordmark abs">veltaro holdings</div>
  </section>

  <section class="letter abs" aria-label="Letterhead">
    <div class="band abs" style="left:0;width:76px"></div>
    <div class="band abs" style="left:335px;width:81px"></div>
    <div class="wordmark abs">veltaro holdings</div>
    <div class="body abs">
      <p>Lorem ipsum dolor sit amet, consectetur adipisicing elit, sed do eiusmod tempor incididunt ut labore et dolore magna aliqua. Ut enim ad minim veniam, quis nostrud exercitation ullamco laboris nisi ut aliquip ex ea commodo consequat. Duis aute irure dolor in reprehenderit in voluptate velit esse cillum dolore eu fugiat nulla pariatur.<br>Excepteur sint occaecat cupidatat non proident, sunt in culpa qui officia deserunt mollit anim id est laborum.</p>
      <p>Proin ac massa sit amet felis egestas rhoncus sit amet at orci. Suspendisse odio lectus, iaculis vel elementum id, facilisis eu erat. Nulla placerat adipiscing enim, non bibendum nibh iaculis vel. Proin ultricies malesuada augue sit amet tempor. Phasellus sit amet mi libero.</p>
      <p>Fusce suscipit odio congue ligula rhoncus vehicula. Ut varius, nisi a ultricies ullamcorper, dolor mi pharetra odio, vel sodales leo dui vel ipsum.</p>
    </div>
    <div class="sign-name abs">Luis R. Andrade</div>
    <div class="signature abs" role="img" aria-label="Handwritten signature of Luis R. Andrade"></div>
    <div class="contact-bar abs">
      <div class="col" style="left:25px">A: Casa de Valdehondo<div class="indent">Calle del Olmo Tardío 42</div><div class="indent">28017 Madrid</div></div>
      <div class="col" style="left:158px">T: +34 (91) 807-3356<br>M: +34 (655) 718-904</div>
      <div class="col" style="left:270px">E: landrade@veltaroholdings.example</div>
    </div>
  </section>

</main>
</body>
</html>
```